Travel agency website refresh

I want to refresh and simplify my current Wordpress.com website. Same general color scheme but modernize and make it user friendly for all devices. Must work with Wordpress. No live booking engines. We are a boutique luxury travel agency. Think luxury, vacation, boho chic, elegant, lush, tropical, cruises, first class. Romance and adventure.
Updates

Target Market(s)

Luxury travelers

Industry/Entity Type

Travel

Coding

Coded - Design and coding required

Number of Pages Required

5+ page

Font styles to use
Sans Serif

Colors
0094D4
00A9DD
6FCCEA
C7EBF8
E9F6FB

Requirements
Must have
• Compatible with Wordpress.com, homepage, about page, contact page, faq page
Nice to have
• The homepage should quickly tell the consumer the type of travel I specialize in. My current website has this (journeyswithmaren.example). I’d like to incorporate the about me as a preview on the home page.
Should not have
• Harsh colors, look generic

```html
<!DOCTYPE html>
<html lang="en">
<head>
<meta charset="utf-8">
<title>Journeys with Maren — Luxury Travel Agent</title>
<link rel="stylesheet" href="https://fonts.googleapis.com/css2?family=Poppins:ital,wght@0,300;0,400;0,500;0,600;0,700;1,400;1,500&display=swap">
<style>
:root{
  --teal:#60c5c8;
  --teal-deep:#3fb4b9;
  --teal-soft:#c7ecee;
  --ink:#1f2a30;
  --ink-soft:#3c4a50;
  --white:#ffffff;
  --paper:#f5f6f6;
  --sky:#e9f6fb;
}
*{box-sizing:border-box;margin:0;padding:0}
html,body{width:1200px;height:4942px;overflow:hidden}
body{position:relative;font-family:"Poppins",sans-serif;color:var(--ink);background:var(--white)}
.abs{position:absolute}
.photo{position:absolute}
.btn-outline{position:absolute;display:flex;align-items:center;justify-content:center;border:2px solid var(--teal);border-radius:40px;font-size:17px;letter-spacing:.5px;color:var(--ink);background:transparent}

/* header */
.site-header{position:absolute;left:0;top:0;width:1200px;height:112px;background:var(--paper)}
.brand{position:absolute;display:flex;align-items:center;gap:10px;font-weight:600;color:var(--teal-deep);font-size:22px;letter-spacing:.5px;white-space:nowrap}
.brand-dot{width:34px;height:34px;border-radius:50%;background:var(--teal)}
.nav{position:absolute;top:38px;left:755px;height:35px;font-size:13px;letter-spacing:.4px}
.nav a{color:var(--ink);text-decoration:none;position:absolute;white-space:nowrap}
.nav .active{color:var(--teal-deep)}
.nav .cta{background:var(--teal);color:var(--white);border-radius:20px;width:113px;height:35px;display:flex;align-items:center;justify-content:center}

/* hero */
.hero{position:absolute;left:0;top:112px;width:1200px;height:691px;background:#eef6fa}
.hero-photo{left:480px;top:0;width:720px;height:691px;
  background:
    linear-gradient(90deg,#eef6fa 0%,rgba(238,246,250,0) 28%),
    radial-gradient(ellipse 120px 260px at 555px 330px,rgba(40,60,110,.55),rgba(40,60,110,0)),
    radial-gradient(ellipse 110px 250px at 215px 320px,rgba(70,110,190,.45),rgba(70,110,190,0)),
    radial-gradient(ellipse 70px 170px at 380px 420px,rgba(220,200,180,.65),rgba(220,200,180,0)),
    linear-gradient(180deg,#dceaf4 0%,#bcd8ec 40%,#9fc9df 52%,#e8ddcc 62%,#dcc9ad 100%)}
.hero-title{position:absolute;left:70px;top:248px;width:510px;text-align:center;font-weight:300;font-size:52px;letter-spacing:9px;color:var(--ink);white-space:nowrap}
.hero-sub{position:absolute;left:70px;top:312px;width:510px;text-align:center;font-size:24px;letter-spacing:17px;color:var(--ink)}

/* about */
.about{position:absolute;left:0;top:803px;width:1200px;height:915px;background:var(--teal);color:var(--white)}
.section-title{font-weight:300;font-size:52px;letter-spacing:1px;line-height:1.15}
.rule{position:absolute;height:2px;width:60px;background:var(--teal-deep)}
.rule::before,.rule::after{content:"";position:absolute;top:-3px;width:8px;height:8px;border-radius:50%;background:inherit}
.rule::before{left:-4px}.rule::after{right:-4px}
.about .rule{background:var(--white)}
.about-lead{position:absolute;left:79px;top:273px;width:560px;font-style:italic;font-weight:500;font-size:12.6px;letter-spacing:.3px;line-height:22.4px;text-transform:uppercase}
.about-hello{position:absolute;left:75px;top:452px;width:560px;font-size:13px;line-height:22px}
.about-sub{position:absolute;left:80px;top:512px;font-size:15.5px;font-weight:500;letter-spacing:.3px}
.about-body{position:absolute;left:75px;top:558px;width:570px;font-size:13px;line-height:22.3px}
.about .btn-outline{border-color:var(--white);color:var(--white)}
.portrait-frame{position:absolute;left:739px;top:234px;width:305px;height:447px;border:2px solid var(--white);border-radius:70px 0 70px 0}
.portrait{left:752px;top:247px;width:280px;height:420px;border-radius:60px 0 60px 0;
  background:radial-gradient(ellipse 100px 130px at 140px 200px,#d99a7c,rgba(217,154,124,0) 100%),
  radial-gradient(ellipse 60px 50px at 140px 400px,#2f4fb0,rgba(47,79,176,0)),
  linear-gradient(160deg,#6b3a26,#9a5a3a 40%,#5a2f1f)}
.socials{position:absolute;left:781px;top:748px;display:flex;gap:14px}
.socials span{width:44px;height:44px;border:2px solid var(--white);border-radius:50%;display:flex;align-items:center;justify-content:center}

/* gallery */
.custom-card{position:absolute;left:432px;top:2100px;width:334px;height:419px;background:linear-gradient(160deg,#8fd3d5,#6fc7c9);color:var(--white);text-align:center;padding:58px 24px 0}
.custom-card h3{font-weight:400;font-size:25px;letter-spacing:.5px;margin-bottom:20px}
.custom-card p{font-size:12.5px;line-height:23px}
.card-arrow{position:absolute;left:152px;top:344px;width:30px;height:30px}

/* caribbean */
.escape-photo{left:0;top:2880px;width:620px;height:653px;
  background:
    linear-gradient(90deg,rgba(255,255,255,0) 55%,#fff 100%),
    radial-gradient(ellipse 110px 260px at 290px 330px,rgba(210,190,160,.9),rgba(210,190,160,0)),
    radial-gradient(ellipse 70px 80px at 200px 540px,rgba(150,150,150,.8),rgba(150,150,150,0)),
    linear-gradient(180deg,#e9eef2 0%,#cfdde6 22%,#9fb8a2 40%,#5f8b5a 62%,#c9c9c4 80%,#e6e4df 100%)}
.escape-title{position:absolute;left:618px;top:2982px;width:580px;font-weight:300;font-size:51px;line-height:64px;letter-spacing:.5px;white-space:nowrap}
.escape-body{position:absolute;left:622px;top:3246px;width:500px;font-size:13px;line-height:22.3px;color:var(--ink-soft)}

/* faq */
.faq-title{position:absolute;left:77px;top:3568px}
.faq-photo{left:618px;top:3729px;width:511px;height:476px;
  background:
    radial-gradient(ellipse 60px 170px at 285px 250px,rgba(232,196,70,.85),rgba(232,196,70,0)),
    radial-gradient(ellipse 60px 170px at 375px 250px,rgba(120,150,175,.75),rgba(120,150,175,0)),
    linear-gradient(180deg,#e6edf1 0%,#eef1f2 30%,#c9b49a 55%,#8a6546 75%,#d9c4a3 100%)}
.faq-item{position:absolute;left:77px;width:664px;border:2px solid var(--teal-soft);background:var(--white);padding:0 26px}
.faq-q{display:flex;justify-content:space-between;align-items:center;height:59px;font-size:16px;letter-spacing:.3px;text-transform:uppercase}
.faq-a{font-size:11.5px;line-height:14px;color:var(--ink-soft);margin-top:-10px}
.toggle{width:18px;height:18px;border-radius:50%;background:var(--teal);position:relative;flex:none}
.toggle::before,.toggle::after{content:"";position:absolute;background:var(--white);left:4px;top:8px;width:10px;height:2px}
.toggle.plus::after{transform:rotate(90deg)}

/* book */
.book-photo{left:0;top:4249px;width:1200px;height:436px;
  background:
    radial-gradient(ellipse 140px 190px at 230px 220px,rgba(60,150,190,.75),rgba(60,150,190,0)),
    radial-gradient(ellipse 170px 60px at 120px 170px,rgba(255,255,255,.85),rgba(255,255,255,0)),
    linear-gradient(180deg,#6fb9dd 0%,#a9d8ee 30%,#2c9fce 50%,#57c0dc 64%,#d9ecf0 74%,#e4d2b4 86%,#d6bf9a 100%)}
.book-title{position:absolute;left:461px;top:4300px;font-weight:700;font-size:40px;color:var(--white);letter-spacing:.5px;white-space:nowrap}
.book-rule{background:var(--white)}
.perk{position:absolute;top:4413px;width:200px;text-align:center;color:var(--white);font-size:17px}
.perk-ring{width:76px;height:76px;margin:0 auto 14px;border-radius:50%;border:3px solid var(--white);background:rgba(96,197,200,.55);display:flex;align-items:center;justify-content:center}
.book-btn{border-color:var(--white);color:var(--white);font-size:16px}

/* footer */
.site-footer{position:absolute;left:0;top:4685px;width:1200px;height:192px;background:var(--paper)}
.contact-chip{position:absolute;top:32px;text-align:center;font-size:17px;letter-spacing:.2px;color:var(--ink-soft)}
.chip-icon{width:64px;height:64px;margin:0 auto 26px;border-radius:50%;border:2px solid var(--teal);display:flex;align-items:center;justify-content:center}
.copyright{position:absolute;left:0;top:4877px;width:1200px;height:65px;background:var(--teal);color:var(--white);font-size:12px;letter-spacing:.5px;display:flex;align-items:center;justify-content:center}
</style>
</head>
<body>

<header class="site-header">
  <div class="brand" style="left:100px;top:38px"><span class="brand-dot"></span>Journeys with Maren</div>
  <nav class="nav">
    <a class="active" style="left:0;top:9px">HOME</a>
    <a style="left:76px;top:9px">ABOUT ME</a>
    <a style="left:182px;top:9px">FAQS</a>
    <a class="cta" style="left:253px;top:0">CONTACT US</a>
  </nav>
</header>

<section class="hero">
  <div class="photo hero-photo" role="img" aria-label="Family of three holding hands, walking on a sunny beach"></div>
  <h1 class="hero-title">LUXURY TRAVEL</h1>
  <p class="hero-sub">AGENT</p>
  <a class="btn-outline" style="left:194px;top:399px;width:225px;height:65px">CONTACT US</a>
</section>

<section class="about">
  <h2 class="section-title abs" style="left:75px;top:140px;color:var(--white)">ABOUT ME</h2>
  <span class="rule" style="left:80px;top:219px"></span>
  <p class="about-lead">I've come nose-to-nose with a giraffe during an African safari. I've strolled along the ancient pathways of Machu Picchu and walked along the Great Wall of China. I've honeymooned in the Australian outback. I've stayed in villas, enjoyed all-inclusive vacations, and gone on cruises and escorted bus tours. Collectively, these experiences—and many, many more—add up to a pretty impressive travel resume but, more importantly, they make me a great choice for your go-to travel agent.</p>
  <p class="about-hello">Hello! My name's Maren Holt, and I'd like to assist you in expertly planning your next vacation—and, hopefully, all those you take in the future.</p>
  <h3 class="about-sub">A LITTLE ABOUT ME &amp; WHY YOU'LL LIKE WORKING WITH ME</h3>
  <p class="about-body">Travel's in my blood! Growing up, my family owned a travel agency and, before I even knew I wanted to be a travel agent, I was off seeing the world—and gaining an appreciation for a well-planned trip. After graduating Northfield Institute of Travel Studies in 1996, I've held management positions with several internationally acclaimed travel companies, gaining a wealth of experience and knowledge that I put to good use when working with clients to design their trips.</p>
  <a class="btn-outline" style="left:75px;top:758px;width:223px;height:67px">KNOW MORE</a>
  <div class="portrait-frame"></div>
  <div class="photo portrait" role="img" aria-label="Portrait of the travel agent"></div>
  <div class="socials" aria-label="Social links">
    <span aria-label="Website"><svg width="20" height="20" viewBox="0 0 20 20"><circle cx="10" cy="10" r="8" fill="none" stroke="#fff" stroke-width="1.8"/><path d="M2 10h16M10 2c3 3 3 13 0 16M10 2c-3 3-3 13 0 16" fill="none" stroke="#fff" stroke-width="1.5"/></svg></span>
    <span aria-label="Email"><svg width="20" height="14" viewBox="0 0 20 14"><rect x="1" y="1" width="18" height="12" rx="2" fill="none" stroke="#fff" stroke-width="2"/><path d="M1 2l9 6 9-6" fill="none" stroke="#fff" stroke-width="2"/></svg></span>
    <span aria-label="Favourites"><svg width="20" height="18" viewBox="0 0 20 18"><path d="M10 16S2 11 2 6a4 4 0 0 1 8-1 4 4 0 0 1 8 1c0 5-8 10-8 10z" fill="none" stroke="#fff" stroke-width="1.8"/></svg></span>
    <span aria-label="Share"><svg width="20" height="20" viewBox="0 0 20 20"><circle cx="5" cy="10" r="2.5" fill="#fff"/><circle cx="15" cy="4" r="2.5" fill="#fff"/><circle cx="15" cy="16" r="2.5" fill="#fff"/><path d="M5 10l10-6M5 10l10 6" stroke="#fff" stroke-width="1.6"/></svg></span>
  </div>
</section>

<section class="gallery">
  <div class="photo" style="left:79px;top:1784px;width:334px;height:503px;background:radial-gradient(ellipse 50px 160px at 90px 250px,rgba(70,100,180,.6),rgba(70,100,180,0)),radial-gradient(ellipse 50px 160px at 270px 260px,rgba(40,60,110,.55),rgba(40,60,110,0)),linear-gradient(180deg,#e3eef6 0%,#c6def0 40%,#a9d3e6 55%,#e6d8c2 68%,#d8c4a6 100%)" role="img" aria-label="Family walking hand in hand along the beach"></div>
  <div class="photo" style="left:79px;top:2306px;width:334px;height:503px;background:radial-gradient(ellipse 70px 180px at 240px 230px,rgba(240,220,215,.9),rgba(240,220,215,0)),linear-gradient(160deg,#3e7a58 0%,#4aa7b8 30%,#e9dcd0 55%,#cfc7b8 75%,#8a8a70 100%)" role="img" aria-label="Couple relaxing in a draped beachside cabana"></div>
  <div class="photo" style="left:432px;top:1784px;width:334px;height:295px;background:linear-gradient(180deg,#5f86b5 0%,#9fb4c8 20%,#b89878 35%,#a37c5c 60%,#d64a4a 70%,#42b6c9 82%,#3aa7c0 100%)" role="img" aria-label="Stone villa with a private pool and loungers"></div>
  <div class="custom-card">
    <h3>CUSTOM TRAVEL</h3>
    <p>A great trip isn't a one-size-fits-all proposition. Rather, your greatest adventures are uniquely your size, reflecting your style and budget. An easy way to get personal when you travel is with customized vacation planning, which can be a private tour</p>
    <svg class="card-arrow" viewBox="0 0 30 30"><circle cx="15" cy="15" r="14" fill="#fff"/><path d="M9 15h11M16 11l4 4-4 4" fill="none" stroke="#60c5c8" stroke-width="2"/></svg>
  </div>
  <div class="photo" style="left:432px;top:2538px;width:334px;height:271px;background:linear-gradient(180deg,#c6d8e6 0%,#b5cadb 18%,#5d8a4c 35%,#7aa05a 55%,#e8ecef 68%,#3b4a5a 82%,#2c3a48 100%)" role="img" aria-label="River cruise ship below a hillside castle"></div>
  <div class="photo" style="left:789px;top:1784px;width:334px;height:503px;background:radial-gradient(ellipse 140px 90px at 170px 260px,rgba(235,235,235,.9),rgba(235,235,235,0)),linear-gradient(180deg,#dfe6ec 0%,#c2d3e2 35%,#b9c6cf 50%,#4f6f93 70%,#8a7a68 85%,#6f6353 100%)" role="img" aria-label="Three friends smiling at a scenic overlook"></div>
  <div class="photo" style="left:789px;top:2306px;width:334px;height:503px;background:linear-gradient(100deg,rgba(0,0,0,0) 55%,#f1f4f7 62%,#c9d3dc 80%,#5f7ea0 100%),linear-gradient(180deg,#dfe8f0 0%,#f3f6f8 15%,#6f8699 28%,#bdd0de 40%,#2ea4d6 55%,#1f93c8 100%)" role="img" aria-label="Cruise ship deck beside snowy mountains and a glacier"></div>
</section>

<section class="escape">
  <div class="photo escape-photo" role="img" aria-label="Woman with a suitcase reading a map on a seaside promenade"></div>
  <h2 class="escape-title">THE BEST PLACES TO<br>RELAX AND UNWIND<br>IN THE CARIBBEAN</h2>
  <span class="rule" style="left:626px;top:3198px;width:92px"></span>
  <p class="escape-body">Something magical happens when Mother Nature puts on a bit of bling. Think of a grown-up, decked-out tree house. Step inside and you connect with nature while, at the same time, you get pampered by all manner of modern comforts and conveniences.</p>
  <a class="btn-outline" style="left:632px;top:3379px;width:205px;height:62px">KNOW MORE</a>
</section>

<section class="faq">
  <h2 class="section-title faq-title">FREQUENTLY ASKED<br>QUESTIONS</h2>
  <span class="rule" style="left:82px;top:3720px;width:100px"></span>
  <div class="photo faq-photo" role="img" aria-label="Two friends in sun hats on a resort beach with loungers"></div>
  <div class="faq-item" style="top:3754px"><div class="faq-q">What is Journeys with Maren?<span class="toggle plus"></span></div></div>
  <div class="faq-item" style="top:3827px;height:128px"><div class="faq-q">Where is your office located?<span class="toggle"></span></div>
    <p class="faq-a">I am located in beautiful Harbor County (USA). Thanks to modern technology, all of our communication can be done via email and phone. If you're local to the Seacoast, you're welcome to request an in-person appointment.</p></div>
  <div class="faq-item" style="top:3969px"><div class="faq-q">Doesn't it cost more to book with a travel agent?<span class="toggle plus"></span></div></div>
  <div class="faq-item" style="top:4040px"><div class="faq-q">Do you charge service fees?<span class="toggle plus"></span></div></div>
  <div class="faq-item" style="top:4118px"><div class="faq-q">Do you charge service fees?<span class="toggle plus"></span></div></div>
</section>

<section class="book">
  <div class="photo book-photo" role="img" aria-label="Couple playfully spinning on a sunny beach by the sea"></div>
  <h2 class="book-title">BOOK YOUR NEXT TRIP WITH US</h2>
  <span class="rule book-rule" style="left:748px;top:4377px;width:92px"></span>
  <div class="perk" style="left:501px"><div class="perk-ring"><svg width="36" height="36" viewBox="0 0 36 36"><circle cx="18" cy="18" r="13" fill="none" stroke="#fff" stroke-width="2.5"/><path d="M18 10v8l6 4" fill="none" stroke="#fff" stroke-width="2.5"/></svg></div>Save Time &amp; Money</div>
  <div class="perk" style="left:697px"><div class="perk-ring"><svg width="36" height="36" viewBox="0 0 36 36"><path d="M10 18l6 6 11-12" fill="none" stroke="#fff" stroke-width="3"/></svg></div>Peace of Mind</div>
  <div class="perk" style="left:900px"><div class="perk-ring"><svg width="36" height="36" viewBox="0 0 36 36"><path d="M18 29s-11-6.5-11-14a6 6 0 0 1 11-3 6 6 0 0 1 11 3c0 7.5-11 14-11 14z" fill="none" stroke="#fff" stroke-width="2.5"/></svg></div>Peace of Mind</div>
  <a class="btn-outline book-btn" style="left:695px;top:4581px;width:196px;height:52px">CONTACT US</a>
</section>

<footer class="site-footer">
  <div class="contact-chip" style="left:165px;width:200px"><div class="chip-icon"><svg width="26" height="26" viewBox="0 0 24 24"><path d="M6.6 10.8a15 15 0 0 0 6.6 6.6l2.2-2.2a1 1 0 0 1 1-.25 11.4 11.4 0 0 0 3.6.57 1 1 0 0 1 1 1V20a1 1 0 0 1-1 1A17 17 0 0 1 3 4a1 1 0 0 1 1-1h3.5a1 1 0 0 1 1 1c0 1.25.2 2.45.57 3.57a1 1 0 0 1-.25 1z" fill="#60c5c8"/></svg></div>555-014-2290</div>
  <div class="brand" style="left:470px;top:72px"><span class="brand-dot"></span>Journeys with Maren</div>
  <div class="contact-chip" style="left:752px;width:340px"><div class="chip-icon"><svg width="26" height="18" viewBox="0 0 20 14"><rect x="1" y="1" width="18" height="12" rx="2" fill="#60c5c8"/><path d="M1 2l9 6 9-6" fill="none" stroke="#fff" stroke-width="1.5"/></svg></div>INFO@JOURNEYSWITHMAREN.EXAMPLE</div>
</footer>
<div class="copyright">COPYRIGHT © 2024 · JOURNEYS WITH MAREN LLC</div>

</body>
</html>
```